" Atendemos de maneira integrada em reabilitação ,tanto odontológica como neurológica. Somos terapia ocupacional, fonoaudiologia, neuropediatria e odontologia. Trabalhamos com técnicas de ponta e muito proximidade com nossos pacientes e suas famílias. "

```html
<!DOCTYPE html>
<html lang="pt-BR">
<head>
<meta charset="utf-8">
<title>Renovatta — cartão de visita</title>
<link rel="stylesheet" href="https://fonts.googleapis.com/css2?family=Roboto:wght@400;500&display=swap">
<style>
  :root {
    --bg: #e9ecef;
    --card: #ffffff;
    --ring: #2e3f7c;
    --brand: #2e3f7c;
    --subtitle: #5b8fd1;
    --text: #333a45;
    --icon: #3f9fc4;
    --icon-glyph: #ffffff;
  }
  html, body {
    margin: 0;
    padding: 0;
    width: 1200px;
    height: 1200px;
    overflow: hidden;
    background: var(--bg);
  }
  .canvas {
    width: 1200px;
    height: 1200px;
    display: block;
  }
  .card-face { fill: var(--card); }
  .card-ring { fill: none; stroke: var(--ring); stroke-width: 9; }
  .brand-name {
    font-family: "Roboto", Arial, sans-serif;
    font-weight: 500;
    font-size: 84px;
    fill: var(--brand);
    letter-spacing: 1px;
  }
  .brand-partners {
    font-family: "Roboto", Arial, sans-serif;
    font-weight: 400;
    font-size: 36px;
    fill: var(--subtitle);
  }
  .contact-line {
    font-family: "Roboto", Arial, sans-serif;
    font-weight: 400;
    font-size: 29px;
    fill: var(--text);
    text-anchor: end;
  }
  .contact-icon { fill: var(--icon); }
  .icon-glyph { fill: none; stroke: var(--icon-glyph); stroke-width: 2.5; stroke-linecap: round; stroke-linejoin: round; }
  .icon-glyph-fill { fill: var(--icon-glyph); }
</style>
</head>
<body>
<svg class="canvas" viewBox="0 0 1200 1200" xmlns="http://www.w3.org/2000/svg">
  <g class="business-card">
    <circle class="card-face" cx="600" cy="600" r="500"/>
    <circle class="card-ring" cx="600" cy="600" r="472"/>

    <g class="brand">
      <text class="brand-name" x="200" y="520">RENOVATTA</text>
      <text class="brand-partners" x="202" y="572">Paulo Mendes &amp; Lívia Araújo</text>
    </g>

    <g class="contacts">
      <g class="contact email">
        <text class="contact-line" x="920" y="646">nome@empresa.com.br</text>
        <circle class="contact-icon" cx="960" cy="636" r="15"/>
        <rect class="icon-glyph" x="951" y="630" width="18" height="12" rx="1.5"/>
        <path class="icon-glyph" d="M951 631 L960 638 L969 631"/>
      </g>
      <g class="contact phone">
        <text class="contact-line" x="920" y="720">99 9999-0000</text>
        <circle class="contact-icon" cx="960" cy="710" r="15"/>
        <rect class="icon-glyph" x="955" y="701" width="10" height="18" rx="2"/>
        <circle class="icon-glyph-fill" cx="960" cy="715" r="1.5"/>
      </g>
      <g class="contact mobile">
        <text class="contact-line" x="920" y="794">99 99999-9999</text>
        <circle class="contact-icon" cx="960" cy="784" r="15"/>
        <circle class="icon-glyph" cx="960" cy="784" r="8"/>
        <path class="icon-glyph" d="M956 781 Q958 788 964 788"/>
      </g>
      <g class="contact address">
        <text class="contact-line" x="920" y="868">Rua do Projeto, 999</text>
        <circle class="contact-icon" cx="960" cy="858" r="15"/>
        <path class="icon-glyph-fill" d="M960 868 C954 861 953 857 953 854 A7 7 0 0 1 967 854 C967 857 966 861 960 868 Z"/>
        <circle class="contact-icon" cx="960" cy="854" r="2.5"/>
      </g>
    </g>
  </g>
</svg>
</body>
</html>
```